Recruitment of Brindle Crew Staffing for the UK market

I want a website for the UK market to attract businesses and companies to come to us for Philipine labour. We want an information site that gives all information on what we do and how we can recruit Philippine labour.
This is a recruitment site for companies to contact us with their requirements for skilled workers coming from the Philipines over to the UK to work.

Target Market(s)

Uk Companies and businesses who want Philipine skilled workers

Industry/Entity Type

REcruitment

Coding

Coded - Design and coding required

Number of Pages Required

5+ page

Font styles to use
Sans Serif

Colors
0054AA
0677BA
7BADD7
CADEEF
E8F1F8
0094D4
00A9DD
6FCCEA
C7EBF8
E9F6FB
EE7325
F08F49
F5BC92
FAE3D3
FDF4ED
EB3D1F
EC4F4E
F09395
F8D3D4
FCEDEE

Requirements
Must have
• Look professional and corperate with drop down menus for Home ,about, services,articles. training , contact us
Nice to have
• Look at Tolvane recruitment- https://tolvanerecruitment.example.co.uk/. This is my current site - https://www.brindlecrewstaffing.example.com/
Should not have
• Cartoons or silly pictures , needs to be corperate looking

```html
<!DOCTYPE html>
<html lang="en">
<head>
<meta charset="utf-8">
<title>Brindle Crew Staffing – Philippine skilled workers for UK companies</title>
<link href="https://fonts.googleapis.com/css2?family=Plus+Jakarta+Sans:wght@400;500;600;700;800&display=swap" rel="stylesheet">
<style>
:root{
  --orange:#EE7325;
  --orange-soft:#F08F49;
  --blue:#1660B6;
  --blue-deep:#0054AA;
  --sky:#CADEEF;
  --mist:#F1F6FC;
  --ink:#111111;
  --text:#333333;
  --muted:#555555;
  --line:#9a9a9a;
  --white:#ffffff;
}
*{box-sizing:border-box;margin:0;padding:0}
html,body{width:1200px;height:4172px;overflow:hidden}
body{position:relative;background:var(--white);font-family:"Plus Jakarta Sans",sans-serif;color:var(--text)}
.abs{position:absolute}
.brand{font-weight:800;font-size:22px;color:var(--blue-deep);display:flex;align-items:center;gap:8px;letter-spacing:-.2px}
.brand-dot{width:14px;height:14px;border-radius:50%;background:var(--orange)}
.nav{top:27px;left:0;width:1200px;height:20px}
.nav a{position:absolute;font-size:14px;color:var(--ink);text-decoration:none;font-weight:500}
.nav a.active{color:var(--orange)}
.accent{color:var(--orange);font-weight:500}
.btn{display:flex;align-items:center;justify-content:space-between;height:36px;border-radius:18px;background:var(--orange);color:#fff;font-size:13.5px;padding:0 5px 0 18px;font-weight:500}
.btn .chev{width:26px;height:26px;border-radius:50%;background:#fff;display:flex;align-items:center;justify-content:center}
.photo{position:absolute}
.p{font-size:13.5px;line-height:22.6px;color:var(--text)}
.hero-title{left:62px;top:228px;font-size:44px;line-height:52px;font-weight:700;color:var(--ink)}
.section-title{font-size:40px;font-weight:700;color:var(--ink)}
.blue-band{left:0;top:1222px;width:1200px;height:693px;background:var(--blue)}
.card{position:absolute;width:338px;height:238px;background:#fff;display:flex;flex-direction:column;align-items:center;justify-content:center;gap:18px;font-weight:700;font-size:18px;color:var(--ink)}
.card svg{width:64px;height:64px}
.role{position:absolute;top:1993px;width:339px;height:337px;overflow:hidden}
.role .bar{position:absolute;left:0;bottom:0;width:100%;height:49px;display:flex;align-items:center;justify-content:space-between;padding:0 20px;color:#fff;font-weight:600;font-size:15px}
.post{position:absolute;left:377px;width:761px}
.post .date{position:absolute;left:0;font-size:12.5px;color:var(--ink);display:flex;align-items:center;gap:10px;font-weight:500}
.post h3{position:absolute;left:2px;width:380px;font-size:18px;line-height:26px;font-weight:700;color:var(--ink)}
.post .p{position:absolute;left:2px;width:380px;font-size:13.5px;line-height:22.6px}
.post .more{position:absolute;left:2px;font-size:13px;color:var(--orange);display:flex;gap:6px;align-items:center}
.post .img{position:absolute;left:423px;width:338px;height:224px}
.rule{position:absolute;left:377px;width:761px;height:1px;background:var(--line)}
.field{position:absolute;left:654px;width:485px;font-size:12.5px;color:var(--ink)}
.field-line{position:absolute;left:652px;width:487px;height:1px;background:#555}
.foot-h{font-size:13px;font-weight:700;color:var(--ink)}
.foot-item{display:flex;gap:12px;align-items:flex-start;font-size:12.5px;line-height:19px;color:var(--ink)}
.social{width:30px;height:30px;border-radius:50%;border:1.5px solid var(--ink)}
</style>
</head>
<body>

<!-- Header -->
<div class="abs brand" style="left:65px;top:22px"><span class="brand-dot"></span>Brindle Crew Staffing</div>
<nav class="abs nav">
  <a class="active" style="left:614px">Home</a>
  <a style="left:696px">About</a>
  <a style="left:779px">Services</a>
  <a style="left:876px">Articles</a>
  <a style="left:967px">Training</a>
  <a style="left:1064px">Contact us</a>
</nav>

<!-- Hero -->
<h1 class="abs hero-title"><span class="accent">Recruiting and placing</span><br>skilled Philippine workers<br>into UK companies</h1>
<p class="abs p" style="left:61px;top:394px;width:520px">Lorem Ipsum is simply dummy text of the printing and typesetting industry. Lorem Ipsum has been the industry's standard dummy text.</p>
<div class="abs btn" style="left:60px;top:474px;width:180px">Contact Us Today<span class="chev"><svg width="10" height="10" viewBox="0 0 10 10"><path d="M3 1l4 4-4 4" fill="none" stroke="#111" stroke-width="1.6"/></svg></span></div>

<div class="photo" role="img" aria-label="Worker operating machinery outdoors" style="left:740px;top:144px;width:129px;height:81px;background:linear-gradient(135deg,#7a6a55,#b9a488)"></div>
<div class="photo" role="img" aria-label="Scientist at a microscope" style="left:873px;top:144px;width:265px;height:81px;background:linear-gradient(135deg,#8fb2d4,#dbe6ef)"></div>
<div class="photo" role="img" aria-label="Chef working in a commercial kitchen" style="left:638px;top:228px;width:191px;height:243px;background:linear-gradient(160deg,#3e5468,#a8a39a)"></div>
<div class="photo" role="img" aria-label="Engineers reviewing plans on a building site" style="left:832px;top:228px;width:368px;height:243px;background:linear-gradient(135deg,#c9c1b4,#8e8879)"></div>
<div class="photo" role="img" aria-label="Team of medical staff" style="left:638px;top:474px;width:261px;height:135px;background:linear-gradient(135deg,#e8eef2,#7fb6cf)"></div>
<div class="photo" role="img" aria-label="Office professionals working at computers" style="left:902px;top:474px;width:298px;height:135px;background:linear-gradient(135deg,#6d7a68,#2f3b4c)"></div>

<!-- About -->
<svg class="abs" style="left:29px;top:725px" width="96" height="72" aria-hidden="true">
  <defs><pattern id="dots" width="8" height="8" patternUnits="userSpaceOnUse"><circle cx="2" cy="2" r="1.5" fill="var(--blue-deep)"/></pattern></defs>
  <rect x="0" y="0" width="96" height="24" fill="url(#dots)"/>
  <rect x="0" y="24" width="24" height="48" fill="url(#dots)"/>
</svg>
<div class="photo" role="img" aria-label="Group of doctors and nurses in a hospital corridor" style="left:60px;top:756px;width:465px;height:390px;background:linear-gradient(135deg,#e4ecf2,#b9d2e4 60%,#eef3f7)"></div>
<h2 class="abs section-title" style="left:594px;top:786px"><span class="accent">What the</span> business is about</h2>
<p class="abs p" style="left:594px;top:841px;width:520px">We source skilled workers directly from the Philippines to work in the UK. With offices , training locations and specialist recruiters we can find the highest quality individuals to add value and resources to any UK business. We delivery quality based on vast experience over a number of years.</p>
<p class="abs p" style="left:594px;top:939px;width:520px">Lorem Ipsum is simply dummy text of the printing and typesetting industry. Lorem Ipsum has been the industry's standard dummy text ever since the 1500s, when an unknown printer took a galley of type and scrambled it to make a type specimen book.</p>
<div class="abs btn" style="left:594px;top:1059px;width:180px">Contact Us Today<span class="chev"><svg width="10" height="10" viewBox="0 0 10 10"><path d="M3 1l4 4-4 4" fill="none" stroke="#111" stroke-width="1.6"/></svg></span></div>

<!-- What We Do -->
<div class="abs blue-band"></div>
<h2 class="abs section-title" style="left:62px;top:1283px;color:#fff"><span class="accent">What</span> We Do</h2>
<p class="abs p" style="left:62px;top:1333px;width:335px;color:#fff">Our company has been estabilished in the Philippines for over 20 years. We have mainly been recruiting philippine workers for the off shore industry in asia but since brexit and the new rules on skilled workers entering the UK we have been working with UK companies who now have chance to recruit...</p>

<div class="card" style="left:431px;top:1284px">
  <svg viewBox="0 0 64 64" fill="none" stroke="var(--blue-deep)" stroke-width="2.5"><circle cx="32" cy="32" r="10"/><path d="M32 10v8M32 46v8M10 32h8M46 32h8M16.5 16.5l5.6 5.6M41.9 41.9l5.6 5.6M16.5 47.5l5.6-5.6M41.9 22.1l5.6-5.6"/></svg>
  Engineer (professional)
</div>
<div class="card" style="left:800px;top:1284px">
  <svg viewBox="0 0 64 64" fill="none" stroke="var(--blue-deep)" stroke-width="2.5"><rect x="14" y="14" width="36" height="36" rx="6"/><path d="M32 22v20M22 32h20"/></svg>
  Health Workers
</div>
<div class="card" style="left:60px;top:1543px">
  <svg viewBox="0 0 64 64" fill="none" stroke="var(--blue-deep)" stroke-width="2.5"><rect x="10" y="12" width="14" height="42" rx="2"/><path d="M24 24h16l10 10M50 34l-6 12M36 54h20"/></svg>
  Welders
</div>
<div class="card" style="left:431px;top:1543px">
  <svg viewBox="0 0 64 64" fill="none" stroke="var(--blue-deep)" stroke-width="2.5"><path d="M20 38c-6-1-10-6-10-12 0-7 6-12 12-11 2-5 6-8 10-8s8 3 10 8c6-1 12 4 12 11 0 6-4 11-10 12v16H20z"/><path d="M20 46h24"/></svg>
  Chef
</div>
<div class="card" style="left:800px;top:1543px">
  <svg viewBox="0 0 64 64" fill="none" stroke="var(--blue-deep)" stroke-width="2.5"><circle cx="20" cy="44" r="10"/><circle cx="48" cy="48" r="6"/><path d="M12 34V20h20l6 14h14v10M30 44h12"/></svg>
  Agriculture
</div>
<div class="abs btn" style="left:512px;top:1823px;width:176px">View All Services<span class="chev"><svg width="10" height="10" viewBox="0 0 10 10"><path d="M3 1l4 4-4 4" fill="none" stroke="#111" stroke-width="1.6"/></svg></span></div>

<!-- How we recruit -->
<h2 class="abs" style="left:62px;top:1992px;font-size:36px;line-height:48px;font-weight:400;color:var(--ink)">how we can recruit<br><span style="color:var(--orange);font-weight:700">Philippine labour</span></h2>
<p class="abs p" style="left:62px;top:2089px;width:340px">We work with companies to find skilled workers that meet the UK requirements for Visas and work permits. We guide you through the whole process and deliver highly trained people that add value to your business.We are here to help both the companies and the Philippino people to gain a better standard of living for their families.</p>

<div class="role" style="left:440px">
  <div role="img" aria-label="Civil engineers in hard hats on site" style="width:100%;height:100%;background:linear-gradient(160deg,#cfd6dc,#8a8f94 60%,#5d5a54)"></div>
  <div class="bar" style="background:var(--blue)">Civil engineer (professional)<svg width="16" height="16" viewBox="0 0 16 16"><path d="M3 13L13 3M5 3h8v8" fill="none" stroke="#fff" stroke-width="2"/></svg></div>
</div>
<div class="role" style="left:800px">
  <div role="img" aria-label="Highways engineer with survey equipment" style="width:100%;height:100%;background:linear-gradient(160deg,#a9c48c,#5f8a3f 60%,#b7d146)"></div>
  <div class="bar" style="background:var(--orange)">Highways engineer<svg width="16" height="16" viewBox="0 0 16 16"><path d="M3 13L13 3M5 3h8v8" fill="none" stroke="#fff" stroke-width="2"/></svg></div>
</div>
<div class="role" style="left:1162px">
  <div role="img" aria-label="Professional role photo" style="width:100%;height:100%;background:linear-gradient(160deg,#9fbbd6,#4e6f91)"></div>
  <div class="bar" style="background:var(--blue)">Petroleum engineer</div>
</div>

<!-- Blog -->
<h2 class="abs" style="left:62px;top:2413px;font-size:38px;line-height:49px;font-weight:700;color:var(--ink)"><span class="accent">Our Recent</span><br>Blog<br>Articles</h2>
<p class="abs p" style="left:62px;top:2566px;width:240px">Lorem Ipsum is simply dummy text of the printing and typesetting industry.</p>
<div class="abs" style="left:62px;top:2654px;font-size:13px;color:var(--orange);display:flex;gap:6px;align-items:center">View All<svg width="10" height="10" viewBox="0 0 10 10"><path d="M2 8L8 2M3.5 2H8v4.5" fill="none" stroke="var(--orange)" stroke-width="1.4"/></svg></div>

<div class="rule" style="top:2419px"></div>
<div class="post" style="top:2445px">
  <div class="date" style="top:14px"><svg width="18" height="18" viewBox="0 0 18 18" fill="none" stroke="var(--orange)" stroke-width="1.4"><rect x="2" y="3" width="14" height="13" rx="2"/><path d="M2 7h14M6 1v4M12 1v4"/></svg>April 20, 2022</div>
  <h3 style="top:48px">Lorem Ipsum is simply dummy text of the printing and typesetting industry.</h3>
  <p class="p" style="top:102px">Lorem Ipsum is simply dummy text of the printing and typesetting industry. Lorem Ipsum has been the industry's standard dummy text.</p>
  <div class="more" style="top:187px">Learn more<svg width="10" height="10" viewBox="0 0 10 10"><path d="M2 8L8 2M3.5 2H8v4.5" fill="none" stroke="var(--orange)" stroke-width="1.4"/></svg></div>
  <div class="img" role="img" aria-label="Factory worker in hard hat beside machinery" style="top:0;background:linear-gradient(135deg,#5a6470,#9aa3ab 60%,#3a3f45)"></div>
</div>
<div class="rule" style="top:2696px"></div>
<div class="post" style="top:2723px">
  <div class="date" style="top:10px"><svg width="18" height="18" viewBox="0 0 18 18" fill="none" stroke="var(--orange)" stroke-width="1.4"><rect x="2" y="3" width="14" height="13" rx="2"/><path d="M2 7h14M6 1v4M12 1v4"/></svg>April 20, 2022</div>
  <h3 style="top:44px">Lorem Ipsum is simply dummy text of the printing and typesetting industry.</h3>
  <p class="p" style="top:100px">Lorem Ipsum is simply dummy text of the printing and typesetting industry. Lorem Ipsum has been the industry's standard dummy text.</p>
  <div class="more" style="top:185px">Learn more<svg width="10" height="10" viewBox="0 0 10 10"><path d="M2 8L8 2M3.5 2H8v4.5" fill="none" stroke="var(--orange)" stroke-width="1.4"/></svg></div>
  <div class="img" role="img" aria-label="Nurse with a patient on a hospital ward" style="top:0;background:linear-gradient(135deg,#d8cfc4,#e07a3e 55%,#f1ece4)"></div>
</div>
<div class="rule" style="top:2977px"></div>
<div class="post" style="top:3008px">
  <div class="date" style="top:10px"><svg width="18" height="18" viewBox="0 0 18 18" fill="none" stroke="var(--orange)" stroke-width="1.4"><rect x="2" y="3" width="14" height="13" rx="2"/><path d="M2 7h14M6 1v4M12 1v4"/></svg>April 20, 2022</div>
  <h3 style="top:44px">Lorem Ipsum is simply dummy text of the printing and typesetting industry.</h3>
  <p class="p" style="top:100px">Lorem Ipsum is simply dummy text of the printing and typesetting industry. Lorem Ipsum has been the industry's standard dummy text.</p>
  <div class="more" style="top:185px">Learn more<svg width="10" height="10" viewBox="0 0 10 10"><path d="M2 8L8 2M3.5 2H8v4.5" fill="none" stroke="var(--orange)" stroke-width="1.4"/></svg></div>
  <div class="img" role="img" aria-label="Businessman working on a laptop in an office" style="top:0;background:linear-gradient(135deg,#eef3f7,#9fc3dc 50%,#2c3440)"></div>
</div>
<div class="rule" style="top:3266px"></div>

<!-- Contact -->
<div class="photo" role="img" aria-label="Map of the Philippines" style="left:0;top:3335px;width:599px;height:531px;background:linear-gradient(160deg,#8aa8ee,#7f9fe8 60%,#94b5d8)"></div>
<div class="abs" style="left:599px;top:3335px;width:601px;height:531px;background:var(--mist)"></div>
<h2 class="abs" style="left:654px;top:3380px;font-size:38px;font-weight:500;color:var(--ink)">Contact Us <span style="color:var(--orange)">Today</span></h2>
<p class="abs p" style="left:654px;top:3431px;width:480px">Please contact us today with your requirements , this can be care workers ,chef, welders, pipe fitters, caravan cabinet makers, medical workers. The UK list of required skills is extensive and the Philippines</p>
<div class="field" style="top:3510px">Name*</div><div class="field-line" style="top:3542px"></div>
<div class="field" style="top:3562px">E-mail*</div><div class="field-line" style="top:3593px"></div>
<div class="field" style="top:3614px">Phone No.*</div><div class="field-line" style="top:3643px"></div>
<div class="field" style="top:3661px">Massage*</div><div class="field-line" style="top:3750px"></div>
<div class="abs btn" style="left:649px;top:3782px;width:118px">Submit<span class="chev"><svg width="10" height="10" viewBox="0 0 10 10"><path d="M3 1l4 4-4 4" fill="none" stroke="#111" stroke-width="1.6"/></svg></span></div>

<!-- Footer -->
<div class="abs brand" style="left:62px;top:3932px"><span class="brand-dot"></span>Brindle Crew Staffing</div>
<p class="abs" style="left:62px;top:3980px;width:290px;font-size:12.5px;line-height:19.5px;color:var(--ink)">We source skilled workers directly from the Philippines to work in the UK. With offices , training locations and specialist recruiters we can find the highest quality individuals to add value and resources to any UK business.</p>

<div class="abs foot-h" style="left:427px;top:3936px">Contact Us</div>
<div class="abs foot-item" style="left:427px;top:3980px;width:300px"><svg width="16" height="18" viewBox="0 0 16 18" fill="none" stroke="var(--orange)" stroke-width="1.5"><path d="M8 17s6-6 6-10A6 6 0 0 0 2 7c0 4 6 10 6 10z"/><circle cx="8" cy="7" r="2"/></svg><span>Larkfield Row, Ashby Vale AV4 2<br>United Kingdom</span></div>
<div class="abs foot-item" style="left:427px;top:4027px"><svg width="16" height="16" viewBox="0 0 16 16" fill="none" stroke="var(--orange)" stroke-width="1.5"><path d="M3 1h3l1.5 4-2 1.5a9 9 0 0 0 4 4L11 8.5l4 1.5v3a2 2 0 0 1-2 2A12 12 0 0 1 1 3a2 2 0 0 1 2-2z"/></svg><span style="font-weight:600">07700 900418</span></div>
<div class="abs foot-item" style="left:427px;top:4059px"><svg width="16" height="14" viewBox="0 0 16 14" fill="none" stroke="var(--orange)" stroke-width="1.5"><rect x="1" y="1" width="14" height="12" rx="1"/><path d="M1 2l7 6 7-6"/></svg><span>sales@brindlecrewstaffing.example.com</span></div>

<div class="abs foot-h" style="left:801px;top:3936px">Subscribe To Our Newsletter:</div>
<div class="abs" style="left:801px;top:3985px;width:337px;height:36px;border:1.5px solid var(--ink);border-radius:18px;overflow:hidden;display:flex">
  <div style="flex:1;font-size:12.5px;color:var(--ink);padding:9px 0 0 20px">E-mail*</div>
  <div style="width:108px;background:var(--orange);color:#fff;font-size:12.5px;display:flex;align-items:center;justify-content:center">Subscribe</div>
</div>
<div class="abs" style="left:801px;top:4044px;display:flex;gap:11px">
  <div class="social"></div><div class="social"></div><div class="social" style="background:var(--orange);border-color:var(--orange)"></div><div class="social"></div>
</div>

<div class="abs" style="left:0;top:4120px;width:1200px;height:1px;background:#cfcfcf"></div>
<div class="abs" style="left:0;top:4142px;width:1200px;text-align:center;font-size:12px;color:var(--ink)">© 2023 All Rights Reserved | Brindle Crew Staffing Ltd</div>

</body>
</html>
```